Wooden Floor Website

I'd like a Modern and crisp site with emphasis on the site being easy to navigate through - services that we offer, gallery of previous work, history, who we are, contact, etc
https://tmqrvx8219067-my.dokshelfbox.net/:b:/g/personal/marcus_bellhaven_co_uk/QWT7K2_pmRsNaHXdovtYBeLWCKjuP9e3F6kRMZbqUwnPzs

Coding

Coded - Design and coding required

Number of Pages Required

5+ page

Requirements
Must have
• Word Press Site

```html
<!DOCTYPE html>
<html lang="en">
<head>
<meta charset="utf-8">
<title>Bellhaven – Exceptional Wood Floors</title>
<link href="https://fonts.googleapis.com/css2?family=Open+Sans:wght@400;600;700&family=Raleway:wght@400;500;600;700;800&display=swap" rel="stylesheet">
<style>
:root{
  --gold:#b08e5b;
  --gold-dark:#8a6c3f;
  --ink:#222;
  --text:#555;
  --muted:#8a8a8a;
  --cream:#f4efe6;
  --dark:#1c1c1c;
  --darker:#111;
  --white:#fff;
  --line:#e3e3e3;
}
*{box-sizing:border-box;margin:0;padding:0}
html,body{width:1200px;height:4337px;overflow:hidden}
body{font-family:"Open Sans",Arial,sans-serif;color:var(--text);background:var(--white);position:relative;font-size:13px;line-height:1.55}
h1,h2,h3,h4,.display{font-family:"Raleway",Arial,sans-serif;color:var(--ink)}
.abs{position:absolute}
.btn{display:inline-block;background:var(--gold);color:#fff;font-family:"Raleway",sans-serif;font-size:12px;font-weight:600;padding:11px 22px;text-decoration:none}
.photo{position:absolute}

/* header */
.topbar{left:0;top:0;width:1200px;height:65px;z-index:3;display:flex;align-items:center;padding:0 40px}
.brand{display:flex;align-items:center;gap:10px;color:#fff;font-family:"Raleway",sans-serif;font-weight:700;font-size:15px;letter-spacing:2px}
.brand .mark{width:22px;height:22px;border:2px solid #fff}
.tagline{position:absolute;left:520px;top:8px;color:#fff;font-size:12px;font-weight:600}
.mail{position:absolute;left:740px;top:8px;color:#fff;font-size:11px}
.nav{position:absolute;right:50px;top:36px;display:flex;gap:20px;color:#fff;font-size:12px;font-family:"Raleway",sans-serif;font-weight:600}
.account{position:absolute;right:50px;top:8px;color:#fff;font-size:11px;display:flex;gap:12px}

/* hero */
.hero{left:0;top:0;width:1200px;height:615px;background:linear-gradient(180deg,#3b2d20 0%,#6b5236 45%,#4a3522 100%)}
.hero-title{left:0;top:115px;width:1200px;text-align:center;color:#fff;font-size:40px;font-weight:800;line-height:1.15;letter-spacing:1px}
.hero-actions{left:0;top:318px;width:1200px;display:flex;justify-content:center;gap:14px}
.features{left:0;top:505px;width:1200px;height:110px;background:rgba(20,14,8,.55);display:flex;justify-content:center;gap:70px;padding-top:22px}
.feature{display:flex;gap:12px;width:260px;color:#ddd;font-size:11px;line-height:1.4}
.feature h4{color:#fff;font-size:13px;font-weight:700;margin-bottom:3px}

/* intro */
.intro-card{left:170px;top:700px;width:320px;height:200px;border:1px solid var(--line);box-shadow:0 2px 10px rgba(0,0,0,.08);padding:22px 26px;font-size:11px}
.intro-card .brand{color:var(--ink);justify-content:center;margin:10px 0 16px}
.intro-card .brand .mark{border-color:var(--gold)}
.intro-body{left:530px;top:700px;width:500px;font-size:12px}
.intro-body h2{font-size:19px;font-weight:700;margin-bottom:10px}
.intro-body .btn{margin-top:18px}

/* experience */
.exp-photo{left:0;top:985px;width:600px;height:460px;background:linear-gradient(135deg,#c9a27a,#a97d4e 60%,#7a5632)}
.exp-panel{left:600px;top:985px;width:600px;height:460px;background:var(--cream);padding:60px 0 0 30px}
.exp-panel h2{color:var(--gold);font-weight:500;font-size:30px;margin-bottom:30px}
.exp-item{display:flex;gap:18px;margin-bottom:30px;width:380px;font-size:11px}
.exp-item svg{flex:none}

/* collection */
.col-head{left:170px;top:1510px;width:860px;display:flex;align-items:center;gap:14px;border-bottom:1px solid var(--line);padding-bottom:10px}
.col-head h3{font-size:17px;font-weight:700;margin-right:20px}
.tab{font-size:11px;padding:6px 14px;background:#e6e6e6;color:#999;font-family:"Raleway",sans-serif}
.tab.active{background:var(--gold);color:#fff}
.col-text{left:170px;top:1625px;width:360px;font-size:12px}
.col-text h2{font-size:30px;font-weight:500;margin-bottom:6px}
.col-text p{margin-bottom:12px}
.swatch{top:1600px;width:140px;height:325px}
.swatch span{position:absolute;left:0;bottom:0;width:100%;background:rgba(0,0,0,.6);color:#fff;font-size:10px;padding:6px 8px}

/* process */
.process{left:0;top:1970px;width:1200px;height:560px;background:linear-gradient(180deg,#9a8162,#7d6546 60%,#6a5439)}
.process-head{left:0;top:2020px;width:1200px;text-align:center;color:#fff}
.process-head h2{color:#fff;font-size:28px;font-weight:700}
.process-head .sub{font-size:12px;margin-bottom:18px}
.process-head p{width:820px;margin:0 auto;font-size:12px;font-weight:600}
.steps{left:170px;top:2225px;width:860px;display:flex;gap:26px}
.step{width:196px;height:250px;background:#1e1e1e;color:#ccc;text-align:center;padding:34px 18px;font-size:12px}
.step svg{margin-bottom:18px}
.step h4{color:#fff;font-size:12px;font-weight:700;padding-bottom:10px;margin-bottom:14px;border-bottom:1px solid #444}

/* projects */
.projects-head{left:0;top:2610px;width:1200px;text-align:center}
.projects-head h2{font-size:32px;font-weight:500}
.projects-head p{font-size:13px}
.project{top:2700px;width:275px;height:235px}
.project span{position:absolute;left:8px;bottom:10px;background:rgba(0,0,0,.65);color:#fff;font-size:11px;padding:6px 12px}
.projects-cta{left:0;top:2990px;width:1200px;text-align:center}

/* help */
.help-band{left:0;top:3108px;width:1200px;height:230px;background:linear-gradient(90deg,#2a1d12,#4b3421 50%,#2c1f14)}
.help-head{left:0;top:3175px;width:1200px;text-align:center;color:#fff}
.help-head .kicker{font-size:13px;color:#ccc}
.help-head h2{color:#fff;font-size:32px;font-weight:500}
.help-photo{left:165px;top:3270px;width:380px;height:620px;background:linear-gradient(160deg,#d9d2c4,#b9a88c 50%,#5c4430)}
.form{left:530px;top:3320px;width:520px;height:550px;background:#fff;box-shadow:0 4px 18px rgba(0,0,0,.12);padding:28px 30px}
.form h4{font-size:13px;font-weight:700;margin-bottom:6px}
.form h4 b{color:var(--gold)}
.form .note{font-size:11px;color:var(--muted);margin-bottom:18px}
.field{height:34px;border:1px solid var(--line);margin-bottom:14px;font-size:11px;color:#aaa;padding:8px 10px}
.field.tall{height:110px}
.submit{height:38px;background:var(--gold);color:#fff;text-align:center;font-size:12px;font-weight:700;line-height:38px;font-family:"Raleway",sans-serif}

/* footer */
.footer{left:0;top:3920px;width:1200px;height:417px;background:var(--dark);color:#aaa;font-size:11px}
.fcol{position:absolute;top:60px}
.fcol h4{color:#fff;font-size:13px;font-weight:700;margin-bottom:14px}
.fcol ul{list-style:none}
.fcol li{margin-bottom:5px}
.fcol li::before{content:"› ";color:var(--gold)}
.fcol .brand{margin-bottom:18px}
.fbottom{position:absolute;left:0;bottom:0;width:1200px;height:62px;background:var(--darker);display:flex;align-items:center;padding:0 165px;justify-content:space-between}
.social{display:flex;align-items:center;gap:10px;color:#fff;font-size:12px}
.social i{width:28px;height:28px;border-radius:50%;border:1px solid #666;display:block}
</style>
</head>
<body>

<div class="abs hero photo" role="img" aria-label="Kitchen with warm oak wood flooring"></div>

<header class="abs topbar">
  <div class="brand"><span class="mark"></span>BELLHAVEN</div>
  <div class="tagline">Creating Exceptional Bespoke Floors</div>
  <div class="mail">enquiries@bellhaven.co.uk</div>
  <div class="account"><span>Register</span><span>Cart</span></div>
  <nav class="nav"><span>Home</span><span>About ▾</span><span>Products ▾</span><span>Work Gallery</span><span>Contact</span></nav>
</header>

<h1 class="abs hero-title">CREATING YOUR<br>EXCEPTIONAL WOOD FLOOR</h1>
<div class="abs hero-actions"><a class="btn">View Our All Products</a><a class="btn">Free Consultation</a></div>

<section class="abs features">
  <div class="feature"><svg width="34" height="34" viewBox="0 0 34 34"><rect x="3" y="3" width="28" height="28" fill="none" stroke="#b08e5b" stroke-width="2"/><path d="M3 17h28M17 3v28" stroke="#b08e5b" stroke-width="2"/></svg><div><h4>DESIGNS &amp; DIMENSIONS</h4>Choose the plank size and pattern that suits your room.</div></div>
  <div class="feature"><svg width="34" height="34" viewBox="0 0 34 34"><path d="M4 28h26M8 28V16M17 28V8M26 28V12" stroke="#b08e5b" stroke-width="2"/></svg><div><h4>GRADING</h4>From prime to rustic grades with knots and character.</div></div>
  <div class="feature"><svg width="34" height="34" viewBox="0 0 34 34"><circle cx="17" cy="17" r="13" fill="none" stroke="#b08e5b" stroke-width="2"/><path d="M9 17h16" stroke="#b08e5b" stroke-width="2"/></svg><div><h4>TEXTURES &amp; TREATMENTS</h4>Brushed, smoked or planed finishes applied with care.</div></div>
</section>

<div class="abs intro-card">
  <div class="brand"><span class="mark"></span>BELLHAVEN</div>
  <p>BELLHAVEN offer a range of fully bespoke finished wood flooring options, herringbone blocks and chevron, made to suit any interior design.</p>
</div>
<div class="abs intro-body">
  <h2>Creating your exceptional wood floors</h2>
  <p>With endless options available, you can choose the design, dimensions, grade, texture, colour and finish of products to achieve the look you want. Combining the finest sustainable oak with the latest state of the art machinery, finishing products and highly skilled craftsmen, we will together create your bespoke wood floor.</p>
  <a class="btn">Read More</a>
</div>

<div class="abs exp-photo photo" role="img" aria-label="Craftsman sanding a herringbone oak floor"></div>
<section class="abs exp-panel">
  <h2>Experience. Integrity. Results.</h2>
  <div class="exp-item"><svg width="40" height="40" viewBox="0 0 40 40"><rect x="1" y="1" width="38" height="38" fill="none" stroke="#b08e5b"/><path d="M12 20l6 6 10-12" stroke="#b08e5b" stroke-width="2" fill="none"/></svg><p>Over two decades fitting fine floors in homes and studios, with care taken on each board we lay for you.</p></div>
  <div class="exp-item"><svg width="40" height="40" viewBox="0 0 40 40"><rect x="1" y="1" width="38" height="38" fill="none" stroke="#b08e5b"/><rect x="12" y="12" width="16" height="16" fill="none" stroke="#b08e5b" stroke-width="2"/></svg><p>Honest advice and clear pricing at every stage, so you always know what goes into your new floor.</p></div>
  <div class="exp-item"><svg width="40" height="40" viewBox="0 0 40 40"><rect x="1" y="1" width="38" height="38" fill="none" stroke="#b08e5b"/><path d="M12 28V18M20 28V12M28 28V22" stroke="#b08e5b" stroke-width="2"/></svg><p>Floors built to last for generations, finished by hand and checked before they leave our workshop.</p></div>
</section>

<div class="abs col-head"><h3>OUR COLLECTION</h3><span class="tab active">PLANK COLLECTION</span><span class="tab">HERRINGBONE COLLECTION</span><span class="tab">CHEVRON COLLECTION</span></div>
<div class="abs col-text">
  <h2>PLANK COLLECTION</h2>
  <p>BELLHAVEN offer you the option of thickness, width and grade in your chosen finish.</p>
  <p>Our range of 28 bespoke finishes are a few of our favourites to whet your appetite, with endless options of textures, colours and finishes available.</p>
  <a class="btn">View All Collection</a>
</div>
<div class="abs swatch photo" style="left:560px;background:linear-gradient(180deg,#8a5b34,#6d4527)" role="img" aria-label="Smoked oak plank sample"><span>BH 001</span></div>
<div class="abs swatch photo" style="left:715px;background:linear-gradient(180deg,#c9a67a,#a8845a)" role="img" aria-label="Natural oak plank sample"><span>BH 014 – Matt</span></div>
<div class="abs swatch photo" style="left:870px;background:linear-gradient(180deg,#3a3230,#221d1b)" role="img" aria-label="Dark stained oak plank sample"><span>BH 027 – Brush</span></div>

<div class="abs process photo" role="img" aria-label="Living room with wide oak planks"></div>
<div class="abs process-head">
  <h2>THE BELLHAVEN PROCESS</h2>
  <div class="sub">Our simple 4 step process allows you to create your own bespoke wood floor.</div>
  <p>Now you've chosen your options our experienced colour technicians will create your wood floor here in the UK, ensuring the highest British quality and prompt delivery. We also offer a bespoke colour matching service to ensure your perfect floor, so please feel free to provide us with a sample you would like us to match.</p>
</div>
<section class="abs steps">
  <div class="step"><svg width="40" height="40" viewBox="0 0 40 40"><rect x="6" y="6" width="28" height="28" fill="none" stroke="#b08e5b" stroke-width="2"/><path d="M6 20h28" stroke="#b08e5b" stroke-width="2"/></svg><h4>CHOOSE YOUR DESIGN</h4>Start creating your bespoke floor by choosing your design</div>
  <div class="step"><svg width="40" height="40" viewBox="0 0 40 40"><path d="M6 34L34 6M6 34h10M6 34V24" stroke="#b08e5b" stroke-width="2" fill="none"/></svg><h4>CHOOSE YOUR DIMENSIONS</h4>Choose the dimensions available in your design</div>
  <div class="step"><svg width="40" height="40" viewBox="0 0 40 40"><path d="M8 32V22M20 32V10M32 32V16" stroke="#b08e5b" stroke-width="2"/></svg><h4>CHOOSE YOUR GRADE</h4>Our range of designs are available in Prime and Rustic grades with the majority of items in stock and ready for finishing</div>
  <div class="step"><svg width="40" height="40" viewBox="0 0 40 40"><circle cx="20" cy="20" r="13" fill="none" stroke="#b08e5b" stroke-width="2"/><path d="M14 20l5 5 8-10" stroke="#b08e5b" stroke-width="2" fill="none"/></svg><h4>CHOOSE YOUR FINISHES</h4>We use UV cured hardwax oil as our final protective layer. Available in Extra Matt, Matt, Satin &amp; Gloss finishes</div>
</section>

<div class="abs projects-head"><h2>Our Projects</h2><p>Gallery Of Previous Work</p></div>
<div class="abs project photo" style="left:170px;background:linear-gradient(160deg,#cfd3d6,#8c8076 60%,#5e4a3a)" role="img" aria-label="Open plan kitchen with oak floor"></div>
<div class="abs project photo" style="left:462px;background:linear-gradient(160deg,#a87a4d,#7a5330 60%,#4f3420)" role="img" aria-label="Kitchen island on warm oak floor"><span>Ashgrove Oak Plank</span></div>
<div class="abs project photo" style="left:755px;background:linear-gradient(160deg,#e4e2dc,#9a8f80 60%,#5a5046)" role="img" aria-label="Bright room with grey oak floor"></div>
<div class="abs projects-cta"><a class="btn">Visit Previous Project Gallery</a></div>

<div class="abs help-band photo" role="img" aria-label="Dark wood floor texture"></div>
<div class="abs help-head"><div class="kicker">Get help now.</div><h2>We are here to Help</h2></div>
<div class="abs help-photo photo" role="img" aria-label="Living room with white sofa on oak floor"></div>
<form class="abs form">
  <h4>Please call <b>+44 (0)1632 960 417</b> if urgent</h4>
  <p class="note">Tell us a little about your project and our team will reply within one working day with advice.</p>
  <div class="field">Name</div>
  <div class="field">Email</div>
  <div class="field">Subject</div>
  <div class="field tall">Message</div>
  <div class="submit">SEND</div>
</form>

<footer class="abs footer">
  <div class="fcol" style="left:165px;width:240px">
    <div class="brand"><span class="mark"></span>BELLHAVEN</div>
    <p>With endless options available, you can choose the design, dimensions, grade, texture, colour and finish of products to achieve the look you want. Combining the finest sustainable oak with the latest state of the art machinery [...]</p>
  </div>
  <div class="fcol" style="left:465px"><h4>Products Selection</h4><ul><li>Designs &amp; Dimensions</li><li>Grading</li><li>Textures &amp; Treatments</li><li>Collections</li><li>Shipping &amp; Returns</li><li>Our Process</li><li>Privacy &amp; Terms</li></ul></div>
  <div class="fcol" style="left:640px"><h4>Site Help</h4><ul><li>Home</li><li>About</li><li>Products</li><li>Work Gallery</li><li>Contact</li></ul></div>
  <div class="fcol" style="left:790px;width:250px"><h4>Address</h4>
    <p style="margin-bottom:8px">Bellhaven Ltd<br>12 Larkspur Road, Wellmont<br>WM4 7QD</p>
    <p style="margin-bottom:8px">+44 (0)1632 960 417</p>
    <p>enquiries@bellhaven.co.uk</p>
  </div>
  <div class="fbottom"><span>© Copyright 2024 Bellhaven | Design by Studio</span><div class="social">Follow Us <i></i><i></i><i></i><i></i></div></div>
</footer>

</body>
</html>
```